fairway fox drywall repair web page

need a web presence for my company. we are a golf themed drywall repair company. need a home page, contact us, photos, about us, services possible payment option

```html
<!DOCTYPE html>
<html lang="en">
<head>
<meta charset="utf-8">
<title>Fairway Fox Drywall Repair</title>
<link href="https://fonts.googleapis.com/css2?family=Roboto:wght@400;500&family=Ubuntu:wght@400;500&display=swap" rel="stylesheet">
<style>
:root{
  --navy:#25306b;
  --yellow:#f2c12e;
  --yellow-dark:#e2ad1a;
  --beige:#f3ead5;
  --band:#efe9e2;
  --text:#555;
  --dark:#1b1b1b;
}
*{margin:0;padding:0;box-sizing:border-box}
html,body{width:746px;height:1200px;overflow:hidden;background:#fff}
body{position:relative;font-family:'Roboto',sans-serif;color:var(--text)}
.abs{position:absolute}
.contact-top{top:39px;font-size:10.5px;color:#555;display:flex;align-items:center;gap:6px}
.brand{left:303px;top:24px;width:140px;display:flex;align-items:center;gap:7px;font-family:'Ubuntu',sans-serif;font-weight:500;font-size:12px;color:var(--navy);line-height:1.15}
.brand-mark{flex:none;width:30px;height:30px;border-radius:50%;background:var(--navy)}
.nav{left:54px;top:86px;width:637px;height:40px;background:linear-gradient(var(--yellow),var(--yellow-dark));display:flex;align-items:center}
.nav a{color:#fff;font-size:9.5px;text-decoration:none;text-transform:uppercase;height:40px;display:flex;align-items:center;justify-content:center}
.nav .home{background:var(--navy);width:86px}
.nav .item{width:98px}
.search{position:absolute;left:504px;top:8px;width:123px;height:22px;background:#fff;border:1px solid #ddd;font-size:8px;color:#777;padding:6px 12px}
.search svg{position:absolute;right:6px;top:4px}
.band{left:0;top:128px;width:746px;height:320px;background:var(--band)}
.hero{left:55px;top:126px;width:636px;height:321px;background:linear-gradient(100deg,#8ea0c4 0%,#d9dde6 35%,#f2f2f2 60%,#e4e4e4 100%);box-shadow:0 8px 10px -6px rgba(0,0,0,.35)}
.hero-title{left:452px;top:198px;font-family:'Ubuntu',sans-serif;font-size:25px;color:var(--navy)}
.hero-title span{color:var(--yellow)}
.hero-sub{left:452px;top:231px;font-family:'Ubuntu',sans-serif;font-size:13.5px;color:#444}
.dots{left:580px;top:432px;display:flex;gap:4px}
.dots i{display:block;width:16px;height:2px;background:#333}
.dots i.on{background:var(--navy)}
.section-title{left:0;width:746px;text-align:center;font-family:'Ubuntu',sans-serif;font-weight:400;font-size:15.5px;color:#555;text-transform:uppercase}
.section-title b{font-weight:400;color:var(--navy)}
.welcome-text{left:60px;top:511px;width:626px;text-align:center;font-size:9.4px;line-height:16.2px;color:#666}
.card{top:662px;width:156px;height:116px;background:var(--navy);text-align:center;color:#fff}
.badge{position:absolute;left:44px;top:-34px;width:68px;height:68px;border-radius:50%;background:var(--yellow);border:3px solid #fff;box-shadow:0 0 0 1px #ddd;display:flex;align-items:center;justify-content:center}
.card h3{margin-top:46px;font-size:9px;font-weight:500;text-transform:uppercase}
.card p{margin:8px 14px 0;font-size:6.6px;line-height:10.8px}
.proj-title{left:53px;top:802px;font-family:'Ubuntu',sans-serif;font-weight:400;font-size:13px;color:#333}
.proj-title b{font-weight:400;color:var(--navy)}
.arrows{left:657px;top:800px;display:flex;gap:3px}
.tile{top:831px;width:154px;height:157px;box-shadow:0 2px 4px rgba(0,0,0,.25);background:linear-gradient(#fff,#e9e9e9)}
.tile .ph{height:121px}
.tile p{text-align:center;font-family:'Ubuntu',sans-serif;font-size:10.5px;color:#333;padding-top:12px}
.footer{left:0;top:1008px;width:746px;height:144px;background:var(--beige)}
.fcol{top:1032px}
.fcol h4{font-family:'Ubuntu',sans-serif;font-weight:400;font-size:10px;color:var(--navy);text-transform:uppercase;margin-bottom:10px}
.fcol p,.fcol li{font-size:6.5px;line-height:12.5px;color:#333}
.links{list-style:none;width:72px}
.links li{border-bottom:1px solid #aaa;padding:0 3px 2px;margin-bottom:5px}
.social{display:flex;align-items:center;gap:6px;margin-bottom:6px;font-size:6.5px;color:#333}
.social i{width:17px;height:17px;border-radius:50%;border:1px solid #777;display:block}
.bottom{left:0;top:1152px;width:746px;height:48px;background:var(--dark);color:#fff;font-size:6.5px;text-align:center;padding-top:20px}
</style>
</head>
<body>
<div class="abs contact-top" style="left:54px">
  <svg width="11" height="11" viewBox="0 0 24 24"><path fill="#25306b" d="M6.6 10.8a15 15 0 0 0 6.6 6.6l2.2-2.2c.3-.3.7-.4 1-.2 1.1.4 2.3.6 3.6.6.6 0 1 .4 1 1V20c0 .6-.4 1-1 1A17 17 0 0 1 3 4c0-.6.4-1 1-1h3.5c.6 0 1 .4 1 1 0 1.3.2 2.5.6 3.6.1.3 0 .7-.2 1z"/></svg>
  +1.555-014-2290
</div>
<div class="abs brand"><span class="brand-mark"></span><span>Fairway Fox<br>Drywall Repair</span></div>
<div class="abs contact-top" style="left:510px">
  <svg width="9" height="12" viewBox="0 0 12 16"><path fill="#25306b" d="M6 0a6 6 0 0 0-6 6c0 4.5 6 10 6 10s6-5.5 6-10a6 6 0 0 0-6-6zm0 8.5A2.5 2.5 0 1 1 6 3.5a2.5 2.5 0 0 1 0 5z"/></svg>
  PO Box 41027, Salem, Oregon 97301
</div>

<div class="abs band"></div>
<nav class="abs nav">
  <a class="home" href="#">Home</a>
  <a class="item" href="#">About Us</a>
  <a class="item" href="#">Photos</a>
  <a class="item" href="#">Services</a>
  <a class="item" href="#">Contact Us</a>
  <div class="search">Search...<svg width="12" height="12" viewBox="0 0 12 12"><circle cx="5" cy="5" r="3.8" fill="none" stroke="#888" stroke-width="1.3"/><path d="M8 8l3 3" stroke="#888" stroke-width="1.5"/></svg></div>
</nav>
<div class="abs hero" role="img" aria-label="Worker in mask and checked shirt smoothing plaster on a wall with a trowel"></div>
<div class="abs hero-title">DRYWALL <span>REPAIR</span></div>
<div class="abs hero-sub">Lorem Ipsum is simply dummy text</div>
<div class="abs dots"><i></i><i class="on"></i><i></i><i></i><i></i></div>

<h2 class="abs section-title" style="top:485px">Welcome to <b>Fairway Fox Drywall Repair</b></h2>
<p class="abs welcome-text">Lorem Ipsum has been the industry's standard dummy text ever since the 1500s, when an unknown printer took a galley of type and scrambled it to make a type specimen book. It has survived not only five centuries, but also the leap into electronic typesetting, remaining essentially unchanged. It was popularised in the 1960s with the release of Letraset sheets containing Lorem Ipsum passages</p>

<h2 class="abs section-title" style="top:592px">Our <b>Service</b></h2>
<div class="abs card" style="left:54px"><div class="badge"><svg width="26" height="26" viewBox="0 0 24 24"><path fill="#fff" d="M21 6.5a5 5 0 0 1-6.6 4.7L6 19.6a2 2 0 0 1-2.8-2.8l8.4-8.4A5 5 0 0 1 17.5 3l-3 3 .6 2.9 2.9.6z"/></svg></div><h3>Repair Services</h3><p>Lorem ipsum dolor sit amet, consectetur adipising elit, sed do eiusmod tempor iunt ut labore et dolore magna</p></div>
<div class="abs card" style="left:215px"><div class="badge"><svg width="24" height="24" viewBox="0 0 24 24"><path fill="#fff" d="M12 3l10 9h-3v9h-5v-6h-4v6H5v-9H2z"/></svg></div><h3>Interior Design Services</h3><p>Lorem ipsum dolor sit amet, consectetur adipising elit, sed do eiusmod tempor iunt ut labore et dolore magna</p></div>
<div class="abs card" style="left:375px"><div class="badge"><svg width="26" height="26" viewBox="0 0 24 24"><path fill="#fff" d="M20 3a3 3 0 0 0-4.2 0l-6 6 4.2 4.2 6-6A3 3 0 0 0 20 3zM8.8 10.4l4.8 4.8-1.4 1.4-1.2-.4L5 22l-3-3 5.8-6 -.4-1.2z"/></svg></div><h3>Drywall Repair</h3><p>Lorem ipsum dolor sit amet, consectetur adipising elit, sed do eiusmod tempor iunt ut labore et dolore magna</p></div>
<div class="abs card" style="left:536px"><div class="badge"><svg width="22" height="26" viewBox="0 0 18 24"><rect x="1" y="1" width="16" height="22" fill="none" stroke="#fff" stroke-width="2"/><g fill="#fff"><rect x="4" y="4" width="2" height="2"/><rect x="8" y="4" width="2" height="2"/><rect x="12" y="4" width="2" height="2"/><rect x="4" y="8" width="2" height="2"/><rect x="8" y="8" width="2" height="2"/><rect x="12" y="8" width="2" height="2"/><rect x="4" y="12" width="2" height="2"/><rect x="8" y="12" width="2" height="2"/><rect x="12" y="12" width="2" height="2"/><rect x="7" y="17" width="4" height="6"/></g></svg></div><h3>Exterior Services</h3><p>Lorem ipsum dolor sit amet, consectetur adipising elit, sed do eiusmod tempor iunt ut labore et dolore magna</p></div>

<h2 class="abs proj-title">OUR <b>PROJECT</b></h2>
<div class="abs arrows">
  <svg width="15" height="15" viewBox="0 0 16 16"><circle cx="8" cy="8" r="7" fill="none" stroke="#222" stroke-width="1.3"/><path d="M9.5 4.5L6 8l3.5 3.5" fill="none" stroke="#222" stroke-width="1.5"/></svg>
  <svg width="15" height="15" viewBox="0 0 16 16"><circle cx="8" cy="8" r="7" fill="none" stroke="#222" stroke-width="1.3"/><path d="M6.5 4.5L10 8l-3.5 3.5" fill="none" stroke="#222" stroke-width="1.5"/></svg>
</div>
<div class="abs tile" style="left:54px"><div class="ph" role="img" aria-label="Scraper peeling wallpaper from a beige wall" style="background:linear-gradient(135deg,#e8dcc4,#c9a878)"></div><p>Ipsum is simply dummy</p></div>
<div class="abs tile" style="left:214px"><div class="ph" role="img" aria-label="Young worker in cap rolling paint onto a patched wall" style="background:linear-gradient(135deg,#c9ccd2,#e8e8e8 60%,#9aa3b8)"></div><p>Ipsum is simply dummy</p></div>
<div class="abs tile" style="left:375px"><div class="ph" role="img" aria-label="Worker in blue shirt and mask lifting a drywall panel" style="background:linear-gradient(135deg,#d8c7a6,#5b86c6 60%,#e6ddd0)"></div><p>Ipsum is simply dummy</p></div>
<div class="abs tile" style="left:535px"><div class="ph" role="img" aria-label="Hammer drill chiselling into a concrete wall" style="background:linear-gradient(135deg,#d4d6d8,#9ba0a6 60%,#c8b9a8)"></div><p>Ipsum is simply dummy</p></div>

<div class="abs footer"></div>
<div class="abs fcol" style="left:57px;width:165px"><h4>Our Works</h4><p>Lorem Ipsum has been the industry's standard dummy text ever since the 1500s, when an unknown printer took a galley of type and scrambled it to make a type specimen book. It has survived not only five centuries, but also the leap into electronic typesetting, remaining essentially unchanged</p></div>
<div class="abs fcol" style="left:275px"><h4>Welcome</h4><ul class="links"><li>About</li><li>Services</li><li>Our works</li><li>Links</li><li style="border:0">Contact</li></ul></div>
<div class="abs fcol" style="left:424px"><h4>Where we are?</h4><p>Fairway Fox Drywall Repair<br>PO Box 41027, Salem, Oregon 97301</p>
  <p style="margin-top:6px"><span style="color:#d55;margin-right:8px">&#9647;</span>555.019.4471</p>
  <p style="margin-top:3px"><span style="color:#d55;margin-right:6px">&#9993;</span>info@fairwayfox.example</p></div>
<div class="abs fcol" style="left:601px"><h4>Follow us on :</h4>
  <div class="social"><i></i>: Friendbook</div>
  <div class="social"><i></i>: Chirper</div>
  <div class="social"><i></i>: Linkwork</div></div>
<div class="abs bottom">Copyright &copy; 2015. . All Rights Reserved</div>
</body>
</html>
```